Web and Logo Design for New Storevane T-shirt Store

I am opening a new online company called Torvelin to sell T-shirts. The website is torvelin.example. For the Menu heading it will be Home, Women, Men, About, Contact, Catalog. For the Categories, it will be Women, Men, T-shirt- Hoodies, Tank Tops, Long Sleeves. I will also need tshirt mockups for the landing page. Footer Menu: Home, About, Contact, Catalog, Shipping and Returns.
The colors to use for the website is #1D7D9E, #Black, #FBC326. For the logo, I will upload examples.
Heading Font: Calistoga.
Body Font: Raleway
Logo Font: Christopher Done.

HERE is an example of how I want my website: mandrel.example, zix.example, frenlo.example, printhollow.example, teeweaver.example.

Target Market(s)

Young people

Industry/Entity Type

Clothing

Coding

Coded - Design and coding required

Number of Pages Required

5+ page

Font styles to use
Sans Serif
Decorative

Colors

Designer to choose colors to be used in the design.

Requirements
Must have
• A unique and creative logo and a stunning homepage.Please look at my website so that you have a feel of what I would like. I want my desgin to have the same page setup as my website.
The colors to use for the website is #1D7D9E, #Black, #FBC326.
Please Look at this link for example: https://shopcrate-lumatheme.storefront.example/
Nice to have
• Tshirt mockups for the homepage, Well use of colors, a homepage slider. A search box.
Should not have
• Don't use basic designs.

```html
<!DOCTYPE html>
<html lang="en">
<head>
<meta charset="utf-8">
<title>Torvelin — T-Shirt Store</title>
<link rel="stylesheet" href="https://fonts.googleapis.com/css2?family=Calistoga&family=Montserrat:wght@500;600;700&family=Raleway:wght@400;500;600;700&display=swap">
<style>
:root{
  --teal:#1D7D9E;
  --yellow:#FBC326;
  --black:#111111;
  --ink:#222222;
  --muted:#8a8a8a;
  --panel:#f4f1ee;
  --line:#e6e6e6;
  --white:#ffffff;
}
*{margin:0;padding:0;box-sizing:border-box}
html,body{width:1200px;height:2792px;overflow:hidden}
body{position:relative;background:var(--white);font-family:'Raleway',sans-serif;color:var(--ink)}
.abs{position:absolute}
.topbar{left:0;top:0;width:1200px;height:30px;background:var(--white);font-size:9px;color:#444}
.topbar .hotline{left:65px;top:10px}
.topbar .social{left:184px;top:13px;display:flex;gap:10px}
.topbar .social i{width:5px;height:5px;border-radius:50%;background:#666;display:block}
.topbar .offer{left:0;width:1200px;top:9px;text-align:center}
.topbar .offer u{color:var(--ink)}
.topbar .cur{left:1065px;top:11px}
.topbar .lang{left:1105px;top:11px}
.topbar .close{left:1178px;top:9px}
.hero{left:0;top:30px;width:1200px;height:818px;background:linear-gradient(90deg,#e4e4e7 0%,#dedee2 60%,#e6e6e9 100%);overflow:hidden}
.hero-photo{left:760px;top:70px;width:330px;height:748px;border-radius:160px 160px 0 0;
  background:linear-gradient(180deg,#5a4236 0%,#6e5444 14%,#c9a692 22%,#b8958a 28%,#232325 34%,#1c1c1e 62%,#2a2a2c 70%,#8fa4bd 74%,#6d89ab 88%,#5f7c9f 100%)}
.logo{font-family:'Montserrat',sans-serif;font-weight:600;font-size:30px;letter-spacing:1px;color:var(--black)}
.hero .logo{left:65px;top:18px}
.nav{top:30px;left:0;font-family:'Montserrat',sans-serif;font-size:8.5px;font-weight:700;letter-spacing:.8px;color:#222}
.nav a{position:absolute;white-space:nowrap;text-decoration:none;color:inherit}
.nav a.active{border-bottom:2px solid var(--yellow);padding-bottom:3px}
.nav-icons{left:1053px;top:26px;display:flex;gap:12px}
.cart-count{left:1123px;top:25px;width:9px;height:9px;border-radius:50%;background:var(--yellow)}
.eyebrow{left:233px;top:130px;font-family:'Montserrat',sans-serif;font-size:22px;font-weight:500;color:var(--teal)}
.hero-title{left:233px;top:160px;font-family:'Montserrat',sans-serif;font-weight:700;font-size:47px;line-height:57px;color:#1a1a1a}
.btn-yellow{left:234px;top:309px;width:100px;height:27px;background:var(--yellow);color:#fff;font-family:'Calistoga',serif;font-size:8.5px;letter-spacing:.3px;display:flex;align-items:center;justify-content:center}
.dots{left:64px;top:273px}
.dots i{position:absolute;left:3px;width:4px;height:4px;border-radius:50%;background:#aaa}
.dots .cur{left:0;top:0;width:9px;height:9px;border:1px solid #555;background:transparent}
.dots .cur::after{content:"";position:absolute;left:9px;top:3px;width:9px;height:1px;background:#555}
.next-thumb{left:227px;top:464px;width:120px;height:180px;background:linear-gradient(180deg,#151515 0%,#1e1e1e 28%,#e9e9e9 40%,#dcdcdc 82%,#1a1a1a 88%,#141414 100%)}
.next-card{left:349px;top:464px;width:116px;height:124px;background:#1f1f1f;color:#fff}
.next-card .lbl{left:13px;top:14px;font-size:8.5px;letter-spacing:2px}
.next-card .lbl svg{vertical-align:middle;margin-left:6px}
.next-card .ttl{left:13px;top:44px;font-family:'Calistoga',serif;font-size:15px;line-height:22px}
.cat-bar{left:158px;top:658px;width:898px;height:125px;background:var(--panel);box-shadow:0 2px 10px rgba(0,0,0,.04)}
.cat{top:46px;display:flex;gap:6px}
.cat svg{flex:none}
.cat h4{font-family:'Montserrat',sans-serif;font-weight:700;font-size:12px;color:#1a1a1a;line-height:15px}
.cat p{font-size:8.5px;color:var(--muted);margin-top:3px}
.section-title{font-family:'Calistoga',serif;font-weight:400;font-size:31px;color:#1a1a1a;text-align:center;left:0;width:1200px}
.product{width:199px}
.product .img{width:199px;height:250px;position:relative}
.product .badge{position:absolute;left:9px;top:9px;height:10px;padding:0 8px;font-size:6.5px;line-height:10px;color:#fff;background:var(--yellow)}
.badge.white{background:#fff;color:#222}
.badge.dark{background:#2b2b2b}
.badge.teal{background:var(--teal)}
.product .name{text-align:center;font-size:9.5px;font-weight:600;color:#333;margin-top:15px}
.product .price{text-align:center;font-size:8.5px;font-weight:700;color:#222;margin-top:8px}
.product .price s{color:#aaa;font-weight:500;margin-right:8px}
.hover-icons{position:absolute;left:0;bottom:12px;width:199px;display:flex;justify-content:center;gap:11px}
.hover-icons i{width:27px;height:27px;border-radius:50%;background:var(--yellow);display:flex;align-items:center;justify-content:center}
.swatches{left:583px;top:1231px;display:flex;gap:5px}
.swatches i{width:8px;height:8px;border-radius:50%;display:block}
.deal{left:65px;top:1656px;width:1069px;height:438px;background:var(--yellow)}
.deal .kicker{left:0;width:536px;top:55px;text-align:center;font-size:11px;color:#333;letter-spacing:.3px}
.deal h2{left:0;width:536px;top:78px;text-align:center;font-family:'Calistoga',serif;font-weight:400;font-size:37px;color:#222}
.deal .old{left:207px;top:138px;font-size:12px;color:#333;text-decoration:line-through}
.deal .btn-outline{left:212px;top:185px;width:100px;height:27px;border:1px solid #333;font-size:8.5px;font-weight:600;display:flex;align-items:center;justify-content:center;color:#222}
.count{top:262px;width:80px;text-align:center}
.count b{display:block;font-family:'Montserrat',sans-serif;font-weight:600;font-size:35px;color:#222;line-height:40px}
.count span{font-size:11.5px;color:#333}
.sep{top:272px;font-size:16px;color:#222}
.deal-photo{left:563px;top:57px;width:468px;height:312px;
  background:linear-gradient(180deg,#f4f4f4 0%,#f0f0f0 20%,rgba(240,240,240,0) 34%),
  linear-gradient(90deg,#efefef 0%,#efefef 22%,#d9d9d9 26%,#f7f7f7 36%,#c8c8c8 46%,#9a9a9a 54%,#2e2e2e 62%,#5a5a5a 68%,#1e1e1e 74%,#262626 78%,#ececec 82%,#efefef 100%)}
.features{left:234px;top:2163px;width:732px;height:124px;border-top:1px solid var(--line);border-bottom:1px solid var(--line)}
.feat{top:57px;display:flex;gap:10px}
.feat h5{font-family:'Montserrat',sans-serif;font-size:9.5px;font-weight:600;color:#222}
.feat p{font-size:8.5px;color:var(--muted);margin-top:5px}
.touch{left:0;width:1200px;top:2356px;text-align:center;font-family:'Montserrat',sans-serif;font-weight:500;font-size:26px;color:#222}
.touch-sub{left:0;width:1200px;top:2395px;text-align:center;font-size:9.5px;color:var(--muted)}
.subscribe{left:451px;top:2437px;width:298px;height:31px;display:flex}
.subscribe .field{flex:1;border:1px solid #ddd;font-size:8.5px;color:#999;padding:11px 12px}
.subscribe .send{width:112px;background:#111;color:#fff;font-size:9px;font-weight:600;display:flex;align-items:center;justify-content:center}
.pay{left:235px;top:2598px;display:flex;gap:5px}
.pay i{width:21px;height:12px;border:1px solid #ddd;border-radius:2px;display:block;background:#f7f7f7}
.foot-logo{left:0;width:1200px;top:2580px;text-align:center}
.legal{left:766px;top:2596px;font-size:9.5px;color:var(--muted)}
.legal b{color:#333;font-weight:500}
.bottom-bar{left:0;top:2714px;width:1200px;height:78px;background:var(--teal);color:#fff;font-size:15.5px;font-weight:500;display:flex;align-items:center;justify-content:center;gap:17px}
</style>
</head>
<body>

<header class="abs topbar">
  <div class="abs hotline">Hotline: +1 555 014 26</div>
  <div class="abs social"><i></i><i></i><i></i></div>
  <div class="abs offer">Special Offer : Winter Sales 50%! <u>Shop Now</u></div>
  <div class="abs cur">$ US</div>
  <div class="abs lang">English</div>
  <svg class="abs close" width="10" height="10" viewBox="0 0 10 10"><path d="M1 1L9 9M9 1L1 9" stroke="#888" stroke-width="1"/></svg>
</header>

<section class="abs hero">
  <div class="abs hero-photo" role="img" aria-label="Young woman with long brown hair wearing a black printed T-shirt and blue jeans"></div>
  <div class="abs logo">Torvelin</div>
  <nav class="abs nav">
    <a class="active" style="left:692px">HOME</a>
    <a style="left:746px">WOMEN</a>
    <a style="left:810px">MEN</a>
    <a style="left:857px">ABOUT</a>
    <a style="left:916px">CONTACT</a>
    <a style="left:987px">CATALOG</a>
  </nav>
  <div class="abs nav-icons">
    <svg width="15" height="15" viewBox="0 0 15 15"><circle cx="6.5" cy="6.5" r="5" fill="none" stroke="#222" stroke-width="1.3"/><path d="M10 10L14 14" stroke="#222" stroke-width="1.3"/></svg>
    <svg width="15" height="15" viewBox="0 0 15 15"><circle cx="7.5" cy="4.5" r="3.3" fill="none" stroke="#222" stroke-width="1.3"/><path d="M1.5 14c0-3.5 2.7-5.5 6-5.5s6 2 6 5.5z" fill="none" stroke="#222" stroke-width="1.3"/></svg>
    <svg width="15" height="15" viewBox="0 0 15 15"><path d="M2 5h11l-1 9H3z" fill="none" stroke="#222" stroke-width="1.3"/><path d="M5 5V3.5a2.5 2.5 0 0 1 5 0V5" fill="none" stroke="#222" stroke-width="1.3"/></svg>
  </div>
  <div class="abs cart-count"></div>

  <div class="abs eyebrow">Collections</div>
  <h1 class="abs hero-title">Women<br>New T-Shirts</h1>
  <div class="abs btn-yellow">SHOP NOW</div>

  <div class="abs dots">
    <i class="cur"></i><i style="top:20px"></i><i style="top:38px"></i><i style="top:57px"></i>
  </div>

  <div class="abs next-thumb" role="img" aria-label="Young man in a white T-shirt against a dark background"></div>
  <div class="abs next-card">
    <div class="abs lbl">NEXT<svg width="32" height="6" viewBox="0 0 32 6"><path d="M0 3h31M27 0.5L31 3L27 5.5" stroke="#fff" stroke-width=".8" fill="none"/></svg></div>
    <div class="abs ttl">Men New<br>T-Shirts...</div>
  </div>

  <div class="abs cat-bar">
    <div class="abs cat" style="left:44px">
      <svg width="28" height="32" viewBox="0 0 28 32" fill="none" stroke="#FBC326" stroke-width="1.3"><circle cx="14" cy="10" r="7"/><path d="M3 31c0-7 5-11 11-11s11 4 11 11z"/></svg>
      <div><h4>WOMEN</h4><p>T-Shirts for Women</p></div>
    </div>
    <div class="abs cat" style="left:210px">
      <svg width="32" height="32" viewBox="0 0 32 32" fill="none" stroke="#FBC326" stroke-width="1.3"><circle cx="16" cy="9" r="7"/><path d="M2 31c0-7 6-11 14-11s14 4 14 11z"/><path d="M16 20v11"/></svg>
      <div><h4>MEN</h4><p>T-Shirts for Men</p></div>
    </div>
    <div class="abs cat" style="left:372px">
      <svg width="28" height="32" viewBox="0 0 28 32" fill="none" stroke="#FBC326" stroke-width="1.3"><path d="M9 2h10l7 6-3 5-2-2v19H7V11l-2 2-3-5z"/><path d="M9 2c0 4 2 7 5 7s5-3 5-7"/><path d="M14 9v21"/></svg>
      <div><h4>T-SHIRT- HOODIES</h4><p>T-Shirts Hoodies</p></div>
    </div>
    <div class="abs cat" style="left:578px">
      <svg width="26" height="32" viewBox="0 0 26 32" fill="none" stroke="#FBC326" stroke-width="1.3"><path d="M6 2v6c0 3-3 6-3 10v13h20V18c0-4-3-7-3-10V2"/><path d="M6 6c3 4 11 4 14 0"/></svg>
      <div><h4>TANK TOPS</h4><p>Tank Top T-Shirts</p></div>
    </div>
    <div class="abs cat" style="left:730px">
      <svg width="34" height="32" viewBox="0 0 34 32" fill="none" stroke="#FBC326" stroke-width="1.3"><path d="M11 2h12l8 6v22h-5V12v18H8V12v18H3V8z"/><path d="M11 2c0 3 3 5 6 5s6-2 6-5"/></svg>
      <div><h4>LONG SLEEVES</h4><p>Long Sleeves T-Shirts</p></div>
    </div>
  </div>
</section>

<h2 class="abs section-title" style="top:862px">Products</h2>

<article class="abs product" style="left:65px;top:931px">
  <div class="img" role="img" aria-label="Man in a dark olive long-sleeve T-shirt with arms crossed" style="background:linear-gradient(180deg,#6f6a61 0%,#5b564d 25%,#4a453d 40%,#3a3630 70%,#2e2b27 100%)"><span class="badge">Hot</span></div>
  <div class="name">Long Sleeves Men T-Shirt</div><div class="price">$20.9</div>
</article>
<article class="abs product" style="left:283px;top:931px">
  <div class="img" role="img" aria-label="Woman seated on pavement in a black graphic T-shirt and light jeans" style="background:linear-gradient(180deg,#d2d1cd 0%,#c3c1bc 30%,#232323 40%,#2a2a2a 58%,#a9b4bd 66%,#c7ccd0 85%,#b9b7b2 100%)"><span class="badge">Hot</span></div>
  <div class="name">Women T-Shirt Model</div><div class="price">$20.9</div>
</article>
<article class="abs product" style="left:501px;top:931px">
  <div class="img" role="img" aria-label="Man in a grey T-shirt on a beach, black and white" style="background:linear-gradient(180deg,#e2e2e2 0%,#cfcfcf 30%,#9b9b9b 42%,#8a8a8a 70%,#626262 85%,#4c4c4c 100%)"><span class="badge white">-15%</span>
    <div class="hover-icons">
      <i><svg width="10" height="10" viewBox="0 0 10 10"><path d="M1 9L9 1M5 1h4v4M1 5v4h4" stroke="#fff" fill="none"/></svg></i>
      <i><svg width="10" height="10" viewBox="0 0 10 10"><path d="M5 9L1.5 5.5a2 2 0 0 1 3.5-3 2 2 0 0 1 3.5 3z" stroke="#fff" fill="none"/></svg></i>
      <i><svg width="10" height="10" viewBox="0 0 10 10"><path d="M1.5 3.5h7l-.7 5.5H2.2z" stroke="#fff" fill="none"/></svg></i>
    </div></div>
  <div class="name">Long Sleeves T-Shirts</div><div class="price"><s>$25.5</s>$20.9</div>
</article>
<article class="abs product" style="left:718px;top:931px">
  <div class="img" role="img" aria-label="Man in a white V-neck T-shirt against black" style="background:linear-gradient(180deg,#111 0%,#191919 28%,#e6e6e6 38%,#dadada 80%,#cfcfcf 92%,#1a1a1a 100%)"><span class="badge">Hot</span></div>
  <div class="name">Men T-Shirts</div><div class="price">$20.9</div>
</article>
<article class="abs product" style="left:936px;top:931px">
  <div class="img" role="img" aria-label="Bearded man in a white printed T-shirt before a carved wooden door" style="background:linear-gradient(180deg,#4a3a30 0%,#5c4637 30%,#ececec 40%,#e2e2e2 82%,#3d3029 90%,#342a24 100%)"><span class="badge dark">New</span></div>
  <div class="name">New T-Shirts</div><div class="price">$20.9</div>
</article>
<div class="abs swatches"><i style="background:#666"></i><i style="background:#f6c7a2;border:1px solid #f3a05f"></i><i style="border:1px solid #ccc"></i></div>

<article class="abs product" style="left:65px;top:1256px">
  <div class="img" role="img" aria-label="Man in a yellow long-sleeve shirt beside a brick building" style="background:linear-gradient(180deg,#6b3a30 0%,#7a4537 28%,#f2a533 38%,#e99a2a 82%,#3b3b3b 90%,#2f2f2f 100%)"><span class="badge">Hot</span></div>
  <div class="name">Long Sleeves Men T-Shirt</div><div class="price">$20.9</div>
</article>
<article class="abs product" style="left:283px;top:1256px">
  <div class="img" role="img" aria-label="Man in a grey V-neck T-shirt, sepia tones" style="background:linear-gradient(180deg,#d4cfc7 0%,#b5afa5 35%,#7c766c 60%,#5f5a52 100%)"><span class="badge">Hot</span></div>
  <div class="name">Long Sleeves Men T-Shirt</div><div class="price">$20.9</div>
</article>
<article class="abs product" style="left:501px;top:1256px">
  <div class="img" role="img" aria-label="Man in a dark maroon T-shirt and jeans on white" style="background:linear-gradient(180deg,#f4f4f4 0%,#ececec 35%,#3e2a2c 42%,#3a2a2c 84%,#5b6f8a 90%,#5b6f8a 100%)"></div>
  <div class="name">Men T-Shirt</div><div class="price">$20.9</div>
</article>
<article class="abs product" style="left:718px;top:1256px">
  <div class="img" role="img" aria-label="Smiling man in a black T-shirt with a red circle print in sunlight" style="background:linear-gradient(180deg,#b8b39a 0%,#8f8a72 30%,#1e1e1e 42%,#8e1d1d 58%,#8e1d1d 72%,#1c1c1c 82%,#1c1c1c 100%)"></div>
  <div class="name">Simple Men T-Shirt</div><div class="price">$20.9</div>
</article>
<article class="abs product" style="left:936px;top:1256px">
  <div class="img" role="img" aria-label="Woman in a red graphic T-shirt on a city rooftop" style="background:linear-gradient(180deg,#d6d8da 0%,#c5c8cb 35%,#d9373c 45%,#c72f35 84%,#5a5c5a 92%,#4d4f4d 100%)"><span class="badge teal">Trend</span></div>
  <div class="name">Simple Women T-Shirt</div><div class="price">$20.9</div>
</article>

<section class="abs deal">
  <div class="abs kicker">DEAL OF THE DAY</div>
  <h2 class="abs">T-Shirts Colection</h2>
  <div class="abs old">$25.5</div>
  <div class="abs btn-outline">SHOP NOW</div>
  <div class="abs count" style="left:53px"><b>01</b><span>Days</span></div>
  <div class="abs sep" style="left:154px">-</div>
  <div class="abs count" style="left:182px"><b>08</b><span>Hours</span></div>
  <div class="abs sep" style="left:284px">-</div>
  <div class="abs count" style="left:312px"><b>22</b><span>Mins</span></div>
  <div class="abs sep" style="left:414px">-</div>
  <div class="abs count" style="left:442px"><b>58</b><span>Secs</span></div>
  <div class="abs deal-photo" role="img" aria-label="Row of white, grey and black T-shirts hanging on a rail against a white wall"></div>
</section>

<section class="abs features">
  <div class="abs feat" style="left:32px">
    <svg width="26" height="16" viewBox="0 0 26 16" fill="none" stroke="#888" stroke-width="1"><path d="M4 2h12v9H4zM16 5h5l3 3v3h-8"/><circle cx="8" cy="13" r="2"/><circle cx="20" cy="13" r="2"/></svg>
    <div><h5>Free Shipping</h5><p>On all orders over $49.00</p></div>
  </div>
  <div class="abs feat" style="left:208px">
    <svg width="16" height="18" viewBox="0 0 16 18" fill="none" stroke="#888" stroke-width="1"><circle cx="8" cy="10" r="7"/><path d="M10 7.5c-.5-1-3.5-1.3-3.8.3s4 1.2 3.7 3.2-3.6 1.4-4 .2M8 5v1.5M8 13.5v1.5"/></svg>
    <div><h5>15 Days Returns</h5><p>Moneyback guarantee</p></div>
  </div>
  <div class="abs feat" style="left:396px">
    <svg width="20" height="16" viewBox="0 0 20 16" fill="none" stroke="#888" stroke-width="1"><rect x="1" y="3" width="18" height="11" rx="1"/><path d="M1 6h18"/></svg>
    <div><h5>Secure Checkout</h5><p>100% Protected by Payvolt</p></div>
  </div>
  <div class="abs feat" style="left:583px">
    <svg width="20" height="16" viewBox="0 0 20 16" fill="none" stroke="#888" stroke-width="1"><rect x="1" y="3" width="18" height="11"/><path d="M8 11l4-6"/><circle cx="8.5" cy="6" r="1"/><circle cx="11.5" cy="10" r="1"/></svg>
    <div><h5>100% Free Warranty</h5><p>Moneyback guarantee</p></div>
  </div>
</section>

<h2 class="abs touch"><svg width="16" height="12" viewBox="0 0 16 12" style="margin-right:6px"><path d="M0 6h14M9 1l5 5-5 5" stroke="#222" stroke-width="1.4" fill="none"/></svg>Get In Touch</h2>
<p class="abs touch-sub">Subscribe for latest stories and promotions (35% sale)</p>
<form class="abs subscribe"><div class="field">Enter your e-mail</div><div class="send">Subscribe</div></form>

<footer>
  <div class="abs pay"><i></i><i></i><i></i><i></i><i></i></div>
  <div class="abs foot-logo"><span class="logo">Torvelin</span></div>
  <div class="abs legal">© 2020 <b>Kelmora</b> · Privacy Policy · Terms of Use</div>
  <nav class="abs bottom-bar">
    <span>Home</span><span>|</span><span>About</span><span>|</span><span>Contact</span><span>|</span><span>Catalog</span><span>|</span><span>Shipping and Returns</span>
  </nav>
</footer>

</body>
</html>
```